Bref créative
Business Cards and Stationary for Law Firm
Voskamp Law Firm
Simple
Marlene Voskamp
Attorney
318 W. Pellington Street
Suite 2700
Corpus Christi, Texas 78455
marlene@voskamplaw.example
www.voskamplaw.example

```html
<!DOCTYPE html>
<html lang="en">
<head>
<meta charset="utf-8">
<title>Voskamp Law Firm — Stationery</title>
<link href="https://fonts.googleapis.com/css2?family=Cinzel:wght@400;600&family=Lato:wght@400;700&display=swap" rel="stylesheet">
<style>
  :root {
    --bg: #2c2c2e;
    --blue-deep: #1336a8;
    --blue: #1f4fd6;
    --blue-light: #3a6cf0;
    --paper: #ffffff;
    --paper-shade: #eef0f4;
    --ink: #2a2f3a;
    --rule: #b9bfcc;
  }
  * { box-sizing: border-box; margin: 0; padding: 0; }
  html, body { width: 1200px; height: 961px; overflow: hidden; background: var(--bg); }
  body { position: relative; font-family: "Lato", sans-serif; color: var(--ink); }

  .piece { position: absolute; box-shadow: 0 8px 24px rgba(0,0,0,.45); }

  /* brand lockup */
  .brand { display: flex; flex-direction: column; align-items: center; font-family: "Cinzel", serif; font-weight: 400; text-align: center; }
  .brand-mark { border: 2px solid currentColor; }
  .brand-name { letter-spacing: .04em; line-height: 1.1; }
  .brand-sub { letter-spacing: .35em; }
  .brand--white { color: var(--paper); }
  .brand--blue { color: var(--blue); }

  /* folder */
  .folder { left: 80px; top: 80px; width: 340px; height: 480px;
    background: linear-gradient(160deg, var(--blue-light), var(--blue) 45%, var(--blue-deep));
    display: flex; align-items: center; justify-content: center; }
  .folder .brand-mark { width: 58px; height: 58px; margin-bottom: 14px; }
  .folder .brand-name { font-size: 30px; }
  .folder .brand-sub { font-size: 11px; margin-top: 6px; }

  /* letterhead */
  .letterhead { left: 450px; top: 80px; width: 340px; height: 480px; background: var(--paper); }
  .letterhead .brand { position: absolute; left: 22px; top: 20px; align-items: flex-start; }
  .letterhead .brand-mark { width: 24px; height: 24px; margin-bottom: 5px; }
  .letterhead .brand-name { font-size: 11px; }
  .letterhead .brand-sub { font-size: 5px; margin-top: 2px; }
  .letterhead-contact { position: absolute; left: 22px; bottom: 44px; font-size: 6.5px; line-height: 1.6; color: var(--ink); }
  .letterhead-band { position: absolute; left: 0; right: 0; bottom: 0; height: 26px;
    background: linear-gradient(90deg, var(--blue-deep), var(--blue-light)); }
  .letterhead-rule { position: absolute; left: 0; right: 0; bottom: 30px; height: 2px; background: var(--rule); }

  /* business cards */
  .card { width: 300px; height: 172px; }
  .card-front { left: 830px; top: 80px; background: var(--paper); }
  .card-front .brand { position: absolute; right: 22px; top: 18px; }
  .card-front .brand-mark { width: 22px; height: 22px; margin-bottom: 4px; }
  .card-front .brand-name { font-size: 11px; }
  .card-front .brand-sub { font-size: 5px; margin-top: 2px; }
  .card-person { position: absolute; left: 22px; top: 72px; }
  .card-person .name { font-family: "Cinzel", serif; font-weight: 600; font-size: 12px; color: var(--blue-deep); letter-spacing: .05em; }
  .card-person .title { font-size: 8px; color: var(--ink); margin-top: 2px; letter-spacing: .1em; text-transform: uppercase; }
  .card-details { position: absolute; left: 22px; top: 106px; font-size: 6.5px; line-height: 1.5; }
  .card-band { position: absolute; left: 0; right: 0; bottom: 0; height: 14px;
    background: linear-gradient(90deg, var(--blue-deep), var(--blue-light)); }
  .card-back { left: 830px; top: 280px;
    background: linear-gradient(160deg, var(--blue-light), var(--blue) 50%, var(--blue-deep));
    display: flex; align-items: center; justify-content: center; }
  .card-back .brand-mark { width: 30px; height: 30px; margin-bottom: 8px; }
  .card-back .brand-name { font-size: 17px; }
  .card-back .brand-sub { font-size: 7px; margin-top: 4px; }

  /* envelope */
  .envelope { left: 80px; top: 620px; width: 560px; height: 260px; background: var(--paper); overflow: hidden; }
  .envelope-band { position: absolute; left: 0; right: 0; top: 0; height: 70px;
    background: linear-gradient(90deg, var(--blue-deep), var(--blue-light)); }
  .envelope .brand { position: absolute; left: 24px; top: 12px; align-items: flex-start; }
  .envelope .brand-mark { width: 20px; height: 20px; margin-bottom: 4px; }
  .envelope .brand-name { font-size: 11px; }
  .envelope .brand-sub { font-size: 5px; margin-top: 2px; }
  .envelope-return { position: absolute; right: 24px; top: 22px; font-size: 7px; line-height: 1.5; color: var(--paper); text-align: right; }
  .envelope-rule { position: absolute; left: 0; right: 0; bottom: 24px; height: 2px; background: var(--rule); }

  /* disc */
  .disc { position: absolute; left: 750px; top: 520px; width: 380px; height: 380px; }
</style>
</head>
<body>

  <section class="piece folder" aria-label="Presentation folder">
    <div class="brand brand--white">
      <span class="brand-mark"></span>
      <span class="brand-name">VOSKAMP</span>
      <span class="brand-sub">LAW FIRM</span>
    </div>
  </section>

  <section class="piece letterhead" aria-label="Letterhead">
    <div class="brand brand--blue">
      <span class="brand-mark"></span>
      <span class="brand-name">VOSKAMP</span>
      <span class="brand-sub">LAW FIRM</span>
    </div>
    <div class="letterhead-contact">
      318 W. Pellington Street<br>
      Suite 2700<br>
      Corpus Christi, Texas 78455<br>
      www.voskamplaw.example
    </div>
    <div class="letterhead-rule"></div>
    <div class="letterhead-band"></div>
  </section>

  <section class="piece card card-front" aria-label="Business card front">
    <div class="brand brand--blue">
      <span class="brand-mark"></span>
      <span class="brand-name">VOSKAMP</span>
      <span class="brand-sub">LAW FIRM</span>
    </div>
    <div class="card-person">
      <div class="name">Marlene Voskamp</div>
      <div class="title">Attorney</div>
    </div>
    <div class="card-details">
      318 W. Pellington Street, Suite 2700<br>
      Corpus Christi, Texas 78455<br>
      Tel 361.555.0142 &nbsp; Fax 361.555.0143<br>
      marlene@voskamplaw.example
    </div>
    <div class="card-band"></div>
  </section>

  <section class="piece card card-back" aria-label="Business card back">
    <div class="brand brand--white">
      <span class="brand-mark"></span>
      <span class="brand-name">VOSKAMP</span>
      <span class="brand-sub">LAW FIRM</span>
    </div>
  </section>

  <section class="piece envelope" aria-label="Envelope">
    <div class="envelope-band"></div>
    <div class="brand brand--white">
      <span class="brand-mark"></span>
      <span class="brand-name">VOSKAMP</span>
      <span class="brand-sub">LAW FIRM</span>
    </div>
    <div class="envelope-return">
      318 W. Pellington Street, Suite 2700<br>
      Corpus Christi, Texas 78455
    </div>
    <div class="envelope-rule"></div>
  </section>

  <svg class="disc" viewBox="0 0 380 380" aria-label="Disc label">
    <defs>
      <linearGradient id="discFill" x1="0" y1="0" x2="1" y2="1">
        <stop offset="0" stop-color="#3a6cf0"/>
        <stop offset=".5" stop-color="#1f4fd6"/>
        <stop offset="1" stop-color="#1336a8"/>
      </linearGradient>
    </defs>
    <circle cx="190" cy="190" r="180" fill="url(#discFill)"/>
    <circle cx="190" cy="190" r="46" fill="#d7dbe3"/>
    <circle cx="190" cy="190" r="20" fill="#2c2c2e"/>
    <rect x="176" y="62" width="28" height="28" fill="none" stroke="#ffffff" stroke-width="2"/>
    <text x="190" y="282" text-anchor="middle" font-family="Cinzel, serif" font-size="22" fill="#ffffff" letter-spacing="1">VOSKAMP</text>
    <text x="190" y="300" text-anchor="middle" font-family="Cinzel, serif" font-size="9" fill="#ffffff" letter-spacing="3">LAW FIRM</text>
  </svg>

</body>
</html>
```